Hornklang Valdora - Sunaders valdorins
Zielgruppe
Amateur-Alphorngruppe, buchbar für Veranstaltungen in Hotels, Auftritte für Hochzeiten, Familienfeiern, Geschäftsessen usw, aber auch Auftritte zu folkloristischen und kulturellen Anlässen und Veranstaltungen im Zusammearbeit mit professionellen Musikern.
Aufgabenstellung
Webseite erstellen mit Hervorheben des Alphorns als Natur- und Hirteninstrument, in der Schweiz zum Nationalsymbol geworden, das aber auch seinen Weg in den Konzertsaal gefunden hat (zusammen mit Klavier, Flöte, Cello). Auftritte auch überall auf der Welt (bsp. in Schweizer Botschaften und in Schweizer Klubs). Bildmaterial über das Engadin und über das Instrument "Alphorn" ist vorhanden. Home - Wir über uns - Repertoire - Unterricht - Kontakt. Zu Rubrik Repertoire können eines oder zwei Musikbeispiele per mp3 geliefert werden.

```html
<!DOCTYPE html>
<html lang="de">
<head>
<meta charset="utf-8">
<title>Hornklang Valdora - Sunaders valdorins</title>
<link href="https://fonts.googleapis.com/css2?family=Source+Sans+3:wght@300;400;600&display=swap" rel="stylesheet">
<style>
:root{
  --wood-dark:#2e1c12;
  --wood-mid:#5a3a26;
  --wood-light:#6e4a32;
  --plank-gap:#1c100a;
  --title:#ecd9cc;
  --nav-bg:#241a14;
  --nav-text:#f4ece6;
  --accent:#e3120b;
  --body-text:#e2d4ca;
  --footer-bg:#1d120c;
  --footer-text:#cbbcb2;
  --grass:#4f7a2c;
  --grass-dark:#2f4a1a;
  --horn:#c89058;
}
*{margin:0;padding:0;box-sizing:border-box}
html,body{width:1200px;height:1120px;overflow:hidden}
body{
  position:relative;
  font-family:"Source Sans 3",sans-serif;
  background:
    repeating-linear-gradient(90deg,
      var(--plank-gap) 0 2px,
      var(--wood-mid) 2px 30px,
      var(--wood-light) 30px 60px,
      var(--wood-mid) 60px 90px,
      var(--wood-dark) 90px 112px),
    var(--wood-mid);
}
body::before{
  content:"";position:absolute;inset:0;
  background:linear-gradient(180deg,rgba(20,10,5,.35),rgba(20,10,5,.1) 40%,rgba(20,10,5,.3));
  pointer-events:none;
}
.site-title{
  position:absolute;top:42px;left:0;width:1200px;text-align:center;padding-left:0;
  font-weight:600;font-size:27px;letter-spacing:.5px;color:var(--title);
}
.main-nav{
  position:absolute;top:112px;left:30px;width:1142px;height:32px;
  background:linear-gradient(180deg,#2c221b,var(--nav-bg));
  box-shadow:0 2px 6px rgba(0,0,0,.5);
}
.main-nav a{
  position:absolute;top:-2px;height:36px;line-height:36px;padding:0 13px;
  font-size:18px;color:var(--nav-text);text-decoration:none;
}
.main-nav a.active{background:var(--accent);}
.hero{
  position:absolute;top:176px;left:48px;width:1072px;height:584px;
  background:
    radial-gradient(ellipse at 50% 45%,rgba(200,144,88,.45),transparent 60%),
    linear-gradient(160deg,var(--grass),var(--grass-dark));
  -webkit-mask-image:radial-gradient(ellipse 55% 60% at 50% 45%,#000 60%,transparent 100%);
  mask-image:radial-gradient(ellipse 55% 60% at 50% 45%,#000 60%,transparent 100%);
  opacity:.9;
}
.band{
  position:absolute;top:762px;left:0;width:1200px;height:3px;background:rgba(20,10,5,.45);
}
.content{position:absolute;top:850px;left:198px;width:820px;}
.content h1{font-weight:400;font-size:18px;color:var(--body-text);letter-spacing:.2px}
.content p{margin-top:19px;font-weight:300;font-size:13px;line-height:19.2px;color:var(--body-text)}
.site-footer{
  position:absolute;top:1086px;left:0;width:1200px;height:34px;background:var(--footer-bg);
}
.site-footer small{position:absolute;left:198px;top:9px;font-size:10px;color:var(--footer-text)}
</style>
</head>
<body>
<header>
  <div class="site-title">HORNKLANG VALDORA</div>
  <nav class="main-nav">
    <a class="active" href="#" style="left:370px">Home</a>
    <a href="#" style="left:441px">Wir über uns</a>
    <a href="#" style="left:566px">Repertoire</a>
    <a href="#" style="left:674px">Unterricht</a>
    <a href="#" style="left:780px">Kontakt</a>
  </nav>
</header>
<div class="hero" role="img" aria-label="Fünf Alphörner aus Holz liegen schräg im sonnigen Gras und werfen Schatten"></div>
<div class="band"></div>
<main class="content">
  <h1>LOREM IPSUM DOLOR SIT AMET</h1>
  <p>consetetur sadipscing elitr, sed diam nonumy eirmod tempor invidunt ut labore et dolore magna aliquyam erat, sed diam voluptua. At vero eos et accusam et justo duo dolores et ea rebum. Stet clita kasd gubergren, no sea takimata sanctus est Lorem ipsum dolor sit amet. Lorem ipsum dolor sit amet, consetetur sadipscing elitr, sed diam nonumy eirmod tempor invidunt ut labore et dolore magna aliquyam erat, sed diam voluptua. At vero eos et accusam et justo duo dolores et ea rebum. Stet clita kasd gubergren, no sea takimata sanctus est Lorem ipsum dolor sit amet.</p>
</main>
<footer class="site-footer"><small>Copyright 2016 www.hornklang-valdora.ch</small></footer>
</body>
</html>
```